LOS PINOS DE ARENA - EXCLUSIVE AND LUXURY REAL ESTATE PROJECT

Se trata del diseño de un mono poste grande (4 m x 2 m) o (8m x 3m) anunciando la construcción de 30 villas de lujo en un terreno en primera línea de playa en el sur de España (Cádiz).

La idea es crear expectación y transmitir lujo y exclusividad.

Target Market(s)

Clientes de alto poder adquisitivo que quieran adquirir su segunda vivienda en un entorno privilegiado a escasos pasos de una de las playas más bonitas de Cádiz.

Industry/Entity Type

REAL ESTATE

Colors

Designer to choose colors to be used in the design.

Requirements
Must have
• LOS PINOS DE ARENA as the name of the development
Nice to have
• Crear expectación con ideas del tipo: “Coming soon” o “No te lo puedes perder”

```html
<!DOCTYPE html>
<html lang="es">
<head>
<meta charset="utf-8">
<title>Los Pinos de Arena</title>
<link href="https://fonts.googleapis.com/css2?family=Cinzel:wght@400&family=Quicksand:wght@600&family=Montserrat:wght@800&display=swap" rel="stylesheet">
<style>
  :root {
    --navy: #02033f;
    --ocean: #0a7ce9;
    --lagoon: #03aeee;
    --white: #ffffff;
  }
  html, body {
    margin: 0;
    padding: 0;
    overflow: hidden;
    background: var(--navy);
  }
  .billboard {
    position: relative;
    width: 1200px;
    height: 674px;
    overflow: hidden;
    background: var(--navy);
  }
  .sea-area {
    position: absolute;
    left: 0;
    right: 0;
    top: 330px;
    bottom: 0;
    background: linear-gradient(to bottom,
      rgba(2, 3, 63, 0) 0%,
      var(--ocean) 45%,
      var(--lagoon) 100%);
  }
  .tagline {
    position: absolute;
    top: 90px;
    left: 0;
    width: 1182px;
    margin: 0;
    text-align: center;
    font-family: "Cinzel", serif;
    font-weight: 400;
    font-size: 46px;
    line-height: 52px;
    letter-spacing: 1px;
    color: var(--white);
  }
  .project-name {
    position: absolute;
    top: 170px;
    left: 0;
    width: 1182px;
    margin: 0;
    text-align: center;
    font-family: "Quicksand", sans-serif;
    font-weight: 600;
    font-size: 140px;
    line-height: 140px;
    letter-spacing: 2px;
    color: var(--white);
    white-space: nowrap;
  }
  .project-name .line {
    display: block;
  }
  .announcement {
    position: absolute;
    top: 508px;
    left: 0;
    width: 1182px;
    margin: 0;
    text-align: center;
    font-family: "Montserrat", sans-serif;
    font-weight: 800;
    font-size: 29px;
    line-height: 40px;
    letter-spacing: 0.5px;
    color: var(--white);
  }
</style>
</head>
<body>
<main class="billboard">
  <div class="sea-area" role="img" aria-label="Bandas onduladas de mar en tonos azules"></div>

  <p class="tagline">LUJO Y EXCLUSIVIDAD</p>

  <h1 class="project-name">
    <span class="line">LOS PINOS</span>
    <span class="line">DE ARENA</span>
  </h1>

  <p class="announcement">
    CONSTRUCCIÓN DE 30 VILLAS DE LUJO<br>
    EN UN TERRENO EN PRIMERA LÍNEA<br>
    DE PLAYA EN EL SUR DE ESPAÑA
  </p>
</main>
</body>
</html>
```